VoIP Unified Communications Service Flyer

I need a trifold brochure made for my VoIP services describing the advantages of switching over to VoIP Unified Communications, I want our current logo, and contact info, as well as the color scheme that we use with the logo, which is gray, and orange, also a picture of the Korvane DXP M41H phone should be used as an example of the phones we provide. The trifold brochure should be printable on 8.5 by 11inch paper, I uploaded some of the images that if modified so I am not plagiarizing, could help for the 3 inner folds.

Target Market(s)

Businesses

Industry/Entity Type

Telecommunications

Font styles to use
Serif
Sans Serif

Requirements
Must have
• Top Reasons to move to VoIP Unified Communications Service, a picture of a Korvane DXP M41H Phone, contact info on the back, company name and logo in the top, one of the reasons should be, we are a local company, and we offer immediate US based support.
Nice to have
• Contact info:

O: (575) 804-3162
C: (575) 462-0571
E: info@pelmorasystems.com
W: https://pelmorasystems.com
FB: https://facebook.com/pelmorasystems

```html
<!DOCTYPE html>
<html lang="en">
<head>
<meta charset="utf-8">
<title>Pelmora Systems – Cloud-Based Phone System Trifold</title>
<link href="https://fonts.googleapis.com/css2?family=Oswald:wght@300;400;500&family=Open+Sans:ital,wght@0,400;0,600;0,700;1,400&display=swap" rel="stylesheet">
<style>
  :root{
    --orange:#e8631c;
    --orange-deep:#d4551a;
    --charcoal:#3b3b3d;
    --charcoal-dark:#2c2c2e;
    --slate:#5a5a5d;
    --paper:#ffffff;
    --paper-soft:#f2f2f2;
    --ink:#3d3d3f;
    --ink-soft:#6b6b6e;
    --backdrop:#e4e4e4;
  }
  *{box-sizing:border-box;margin:0;padding:0}
  html,body{width:1200px;height:2402px;overflow:hidden;background:var(--backdrop)}
  body{font-family:"Open Sans",Arial,sans-serif;color:var(--ink)}
  .canvas{position:relative;width:1200px;height:2402px;overflow:hidden;background:var(--backdrop)}

  .sheet{position:absolute;height:742px;display:flex;box-shadow:0 10px 28px rgba(0,0,0,.18)}
  .sheet--cover{top:29px;left:440px}
  .sheet--outside{top:829px;left:120px}
  .sheet--inside{top:1630px;left:120px}
  .panel{position:relative;width:320px;height:742px;overflow:hidden;background:var(--paper)}

  /* brand */
  .brand{display:flex;align-items:center;gap:8px;font-family:"Oswald",sans-serif;font-weight:500;
    font-size:17px;letter-spacing:1.2px;text-transform:uppercase;color:var(--orange);white-space:nowrap}
  .brand__dot{width:14px;height:14px;border-radius:50%;background:var(--slate);flex:none}
  .brand--on-dark .brand__dot{background:#8a8a8d}

  .photo{position:absolute}
  .shape{position:absolute;left:0;width:320px}

  /* cover */
  .cover__brand{position:absolute;top:28px;left:26px}
  .cover__photo{top:70px;left:0;width:320px;height:420px;
    background:radial-gradient(ellipse at 72% 38%,#f7c48a 0%,#d98d55 14%,rgba(170,160,150,.6) 38%,rgba(220,222,224,0) 70%),
               linear-gradient(180deg,#f5f5f5 0%,#d9dbdd 45%,#8e9196 75%,#55585c 100%)}
  .cover__headline{position:absolute;top:548px;left:30px;font-family:"Oswald",sans-serif;text-transform:uppercase;line-height:1.14}
  .cover__headline .lead{display:block;color:var(--orange);font-weight:400;font-size:31px;letter-spacing:.5px}
  .cover__headline .rest{display:block;color:#fff;font-weight:300;font-size:31px;letter-spacing:.5px}
  .web-bar{position:absolute;left:0;bottom:0;width:100%;height:46px;background:var(--orange);
    display:flex;align-items:center;gap:9px;padding-left:26px;color:#fff;font-size:14px;font-weight:600}
  .web-bar svg{flex:none}

  /* outside left: features */
  .features{background:var(--charcoal)}
  .features__photo{top:0;left:0;width:320px;height:170px;clip-path:polygon(0 0,100% 0,100% 45%,0 100%);
    background:linear-gradient(135deg,#c9b9a3 0%,#a08668 40%,#e9e4dc 100%)}
  .features__list{position:absolute;top:190px;left:26px;right:22px;list-style:none}
  .feature{display:grid;grid-template-columns:26px 1fr;column-gap:10px;margin-bottom:20px}
  .feature__icon{width:26px;height:26px;border-radius:4px;background:var(--orange);display:flex;align-items:center;justify-content:center}
  .feature__title{font-family:"Oswald",sans-serif;font-size:14px;color:var(--orange);text-transform:uppercase;letter-spacing:.6px;line-height:1.1}
  .feature__text{grid-column:2;font-size:9.5px;line-height:1.45;color:#e3e3e3;margin-top:3px}

  /* outside middle: back */
  .back__hex{position:absolute;top:28px;left:55px;width:210px;height:226px;background:var(--orange);
    clip-path:polygon(50% 0,100% 25%,100% 75%,50% 100%,0 75%,0 25%)}
  .back__hex-inner{position:absolute;inset:12px;clip-path:polygon(50% 0,100% 25%,100% 75%,50% 100%,0 75%,0 25%);
    background:linear-gradient(150deg,#f4f4f4 0%,#d6d6d6 40%,#3a3a3a 60%,#1f1f1f 100%)}
  .back__brand{position:absolute;top:330px;left:34px}
  .back__values{position:absolute;top:372px;left:34px;right:30px;font-style:italic;font-size:11.5px;line-height:1.55;color:#ededed}
  .contact{position:absolute;top:600px;left:30px;right:20px;color:#fff;font-size:11px;font-weight:600}
  .contact__row{display:flex;align-items:center;gap:9px;margin-bottom:9px}
  .contact__icon{width:20px;height:20px;border-radius:50%;background:#fff;display:flex;align-items:center;justify-content:center;flex:none}
  .social{position:absolute;top:566px;left:150px;display:flex;gap:8px}
  .social span{width:20px;height:20px;border-radius:50%;border:1.5px solid #fff}

  /* inside left: benefits */
  .benefits__photo{top:0;left:0;width:320px;height:190px;
    background:linear-gradient(120deg,#e8b98c 0%,#f1d6b8 35%,#8aa9c4 70%,#d7dde3 100%)}
  .benefits__hex{position:absolute;top:150px;left:18px;width:104px;height:112px;background:var(--orange);
    clip-path:polygon(50% 0,100% 25%,100% 75%,50% 100%,0 75%,0 25%)}
  .benefits__hex-inner{position:absolute;inset:8px;clip-path:polygon(50% 0,100% 25%,100% 75%,50% 100%,0 75%,0 25%);
    background:linear-gradient(150deg,#f0f0f0 0%,#bdbdbd 45%,#2a2a2a 65%,#1c1c1c 100%)}
  .benefits__heading{position:absolute;top:262px;left:0;width:220px;height:30px;background:var(--charcoal);
    clip-path:polygon(0 0,88% 0,100% 100%,0 100%);color:#fff;font-size:13px;padding:6px 0 0 26px}
  .checklist{position:absolute;left:24px;right:20px;list-style:none}
  .benefits .checklist{top:306px}
  .check{display:grid;grid-template-columns:15px 1fr;column-gap:8px;margin-bottom:13px}
  .check__tick{width:15px;height:15px;border-radius:50%;background:var(--charcoal);display:flex;align-items:center;justify-content:center;margin-top:1px}
  .check__title{font-size:11px;font-weight:700;color:var(--orange)}
  .check__text{grid-column:2;font-size:9.5px;line-height:1.45;color:var(--ink);margin-top:1px}

  /* inside middle: services */
  .services{background:var(--charcoal)}
  .services__brand{position:absolute;top:30px;left:40px}
  .services__heading{position:absolute;top:66px;left:40px;font-family:"Oswald",sans-serif;font-size:15px;letter-spacing:1.5px;color:#fff;text-transform:uppercase}
  .services__list{position:absolute;top:112px;left:26px;right:20px;list-style:none}
  .service{display:grid;grid-template-columns:44px 1fr;column-gap:14px;margin-bottom:22px;align-items:start}
  .service__icon{width:44px;height:48px;background:var(--orange);clip-path:polygon(50% 0,100% 25%,100% 75%,50% 100%,0 75%,0 25%);
    display:flex;align-items:center;justify-content:center}
  .service__title{font-family:"Oswald",sans-serif;font-size:13px;color:var(--orange);text-transform:uppercase;letter-spacing:.6px}
  .service__text{font-size:9.5px;line-height:1.45;color:#d9d9d9;margin-top:2px}

  /* inside right: features continued */
  .extras .checklist{top:28px}
  .extras__photo{top:520px;left:0;width:320px;height:222px;clip-path:polygon(0 22%,62% 0,100% 12%,100% 100%,0 100%);
    background:linear-gradient(160deg,#d7dce2 0%,#8f99a4 45%,#3d4550 100%)}
</style>
</head>
<body>
<main class="canvas">

  <!-- Folded front cover -->
  <section class="sheet sheet--cover" aria-label="Brochure front cover">
    <article class="panel cover">
      <div class="brand cover__brand"><span class="brand__dot"></span>Pelmora Systems</div>
      <div class="photo cover__photo" role="img" aria-label="Businesswoman standing by a window with a network of connected contact icons"></div>
      <svg class="shape" style="top:400px;height:342px" viewBox="0 0 320 342" aria-hidden="true">
        <polygon points="0,96 320,0 320,24 0,120" fill="#6a6a6d"/>
        <polygon points="0,120 320,24 320,342 0,342" fill="#3b3b3d"/>
      </svg>
      <h1 class="cover__headline"><span class="lead">A Cloud-Based</span><span class="rest">Phone System for</span><span class="rest">Businesses</span></h1>
      <div class="web-bar">
        <svg width="14" height="14" viewBox="0 0 14 14"><circle cx="7" cy="7" r="6" fill="none" stroke="#fff" stroke-width="1.5"/><path d="M1 7h12M7 1c-3 3-3 9 0 12M7 1c3 3 3 9 0 12" fill="none" stroke="#fff" stroke-width="1"/></svg>
        www.pelmorasystems.com
      </div>
    </article>
  </section>

  <!-- Outside spread -->
  <section class="sheet sheet--outside" aria-label="Brochure outside spread">
    <article class="panel features">
      <div class="photo features__photo" role="img" aria-label="Team working together around an office desk"></div>
      <ul class="features__list">
        <li class="feature">
          <span class="feature__icon"><svg width="14" height="14" viewBox="0 0 14 14"><path d="M2 12V7M6 12V4M10 12V1" stroke="#fff" stroke-width="2"/></svg></span>
          <h3 class="feature__title">Scalable</h3>
          <p class="feature__text">Add new lines as your company grows and only pay for the users you actually need.</p>
        </li>
        <li class="feature">
          <span class="feature__icon"><svg width="14" height="14" viewBox="0 0 14 14"><circle cx="7" cy="7" r="5.5" fill="none" stroke="#fff" stroke-width="1.6"/><path d="M7 3.5v7M5 5.5h3a1 1 0 010 2H6a1 1 0 000 2h3" fill="none" stroke="#fff" stroke-width="1.2"/></svg></span>
          <h3 class="feature__title">Surprisingly Affordable</h3>
          <p class="feature__text">Flat-rate plans save most businesses up to 60% on their monthly phone bill.</p>
        </li>
        <li class="feature">
          <span class="feature__icon"><svg width="14" height="14" viewBox="0 0 14 14"><path d="M7 1l1.8 3.8 4.2.5-3.1 2.9.8 4.1L7 10.3 3.3 12.3l.8-4.1L1 5.3l4.2-.5z" fill="#fff"/></svg></span>
          <h3 class="feature__title">Amazing Service</h3>
          <p class="feature__text">We are a local company and offer immediate US based support whenever you call.</p>
        </li>
        <li class="feature">
          <span class="feature__icon"><svg width="14" height="14" viewBox="0 0 14 14"><path d="M7 1l5 2v4c0 3-2.3 5-5 6-2.7-1-5-3-5-6V3z" fill="#fff"/></svg></span>
          <h3 class="feature__title">Reliable</h3>
          <p class="feature__text">Always stay connected with redundant data centers and 99.99% network uptime.</p>
        </li>
        <li class="feature">
          <span class="feature__icon"><svg width="14" height="14" viewBox="0 0 14 14"><rect x="2" y="2" width="10" height="4" rx="1" fill="#fff"/><rect x="2" y="8" width="10" height="4" rx="1" fill="#fff"/></svg></span>
          <h3 class="feature__title">Hosted PBX</h3>
          <p class="feature__text">Make calls and manage your whole phone system from anywhere, on any device.</p>
        </li>
      </ul>
      <div class="web-bar" style="height:38px;font-size:12px">
        <svg width="12" height="12" viewBox="0 0 14 14"><circle cx="7" cy="7" r="6" fill="none" stroke="#fff" stroke-width="1.5"/><path d="M1 7h12" stroke="#fff"/></svg>
        www.pelmorasystems.com
      </div>
    </article>

    <article class="panel back">
      <svg class="shape" style="top:0;height:742px" viewBox="0 0 320 742" aria-hidden="true">
        <polygon points="0,300 320,230 320,742 0,742" fill="#3b3b3d"/>
        <polygon points="0,560 140,520 320,560 320,742 0,742" fill="#e8631c"/>
      </svg>
      <div class="back__hex"><div class="back__hex-inner" role="img" aria-label="Korvane DXP M41H desk phone with handset and display"></div></div>
      <div class="brand back__brand brand--on-dark"><span class="brand__dot"></span>Pelmora Systems</div>
      <p class="back__values">Customer satisfaction, openness, innovation, teamwork and growth are the core values behind our company. We continue to reflect who we are, how we work and what we stand for.</p>
      <div class="social" aria-label="Social channels"><span></span><span></span></div>
      <div class="contact">
        <div class="contact__row">
          <span class="contact__icon"><svg width="11" height="11" viewBox="0 0 12 12"><path d="M3 1l2 2.5-1.2 1.2a7 7 0 003.5 3.5L8.5 7 11 9l-1.5 2C5 11 1 7 1 2.5z" fill="#e8631c"/></svg></span>
          (575) 804-3162 &nbsp;|&nbsp; (575) 462-0571
        </div>
        <div class="contact__row">
          <span class="contact__icon"><svg width="11" height="11" viewBox="0 0 12 12"><rect x="1" y="2.5" width="10" height="7" fill="none" stroke="#e8631c" stroke-width="1.4"/><path d="M1 3l5 3.5L11 3" fill="none" stroke="#e8631c" stroke-width="1.2"/></svg></span>
          info@pelmorasystems.com
        </div>
        <div class="contact__row">
          <span class="contact__icon"><svg width="11" height="11" viewBox="0 0 14 14"><circle cx="7" cy="7" r="5.5" fill="none" stroke="#e8631c" stroke-width="1.5"/><path d="M1.5 7h11M7 1.5c-2.6 3-2.6 8 0 11M7 1.5c2.6 3 2.6 8 0 11" fill="none" stroke="#e8631c"/></svg></span>
          www.pelmorasystems.com
        </div>
      </div>
    </article>

    <article class="panel cover">
      <div class="brand cover__brand"><span class="brand__dot"></span>Pelmora Systems</div>
      <div class="photo cover__photo" role="img" aria-label="Businesswoman standing by a window with a network of connected contact icons"></div>
      <svg class="shape" style="top:400px;height:342px" viewBox="0 0 320 342" aria-hidden="true">
        <polygon points="0,96 320,0 320,24 0,120" fill="#6a6a6d"/>
        <polygon points="0,120 320,24 320,342 0,342" fill="#3b3b3d"/>
      </svg>
      <h2 class="cover__headline"><span class="lead">A Cloud-Based</span><span class="rest">Phone System for</span><span class="rest">Businesses</span></h2>
      <div class="web-bar">
        <svg width="14" height="14" viewBox="0 0 14 14"><circle cx="7" cy="7" r="6" fill="none" stroke="#fff" stroke-width="1.5"/><path d="M1 7h12M7 1c-3 3-3 9 0 12M7 1c3 3 3 9 0 12" fill="none" stroke="#fff" stroke-width="1"/></svg>
        www.pelmorasystems.com
      </div>
    </article>
  </section>

  <!-- Inside spread -->
  <section class="sheet sheet--inside" aria-label="Brochure inside spread">
    <article class="panel benefits">
      <div class="photo benefits__photo" role="img" aria-label="Smiling professional talking on an office phone at her desk"></div>
      <div class="benefits__hex"><div class="benefits__hex-inner" role="img" aria-label="Korvane DXP M41H desk phone"></div></div>
      <h3 class="benefits__heading">Phone benefits</h3>
      <ul class="checklist">
        <li class="check"><span class="check__tick"><svg width="8" height="8" viewBox="0 0 8 8"><path d="M1 4l2 2 4-4" fill="none" stroke="#fff" stroke-width="1.5"/></svg></span>
          <h4 class="check__title">Saves you money</h4>
          <p class="check__text">Customers of Halvern small business VoIP phone service typically experience savings of up to 60% on their monthly phone bill.</p></li>
        <li class="check"><span class="check__tick"><svg width="8" height="8" viewBox="0 0 8 8"><path d="M1 4l2 2 4-4" fill="none" stroke="#fff" stroke-width="1.5"/></svg></span>
          <h4 class="check__title">Scalable network</h4>
          <p class="check__text">A scalable network developed by over 1,500 engineers powers Halvern business VoIP phone service. We promise top quality, security, and reliability.</p></li>
        <li class="check"><span class="check__tick"><svg width="8" height="8" viewBox="0 0 8 8"><path d="M1 4l2 2 4-4" fill="none" stroke="#fff" stroke-width="1.5"/></svg></span>
          <h4 class="check__title">Designed for all industries</h4>
          <p class="check__text">There's something for everyone. Our small business cloud VoIP features benefit all industries, including insurance, hospitality, consulting firms, real estate, education, health care, and more!</p></li>
        <li class="check"><span class="check__tick"><svg width="8" height="8" viewBox="0 0 8 8"><path d="M1 4l2 2 4-4" fill="none" stroke="#fff" stroke-width="1.5"/></svg></span>
          <h4 class="check__title">Innovation</h4>
          <p class="check__text">We are always innovating and improving our VoIP phone service. Your small business will always have the latest and greatest in business VoIP technology and phone systems.</p></li>
        <li class="check"><span class="check__tick"><svg width="8" height="8" viewBox="0 0 8 8"><path d="M1 4l2 2 4-4" fill="none" stroke="#fff" stroke-width="1.5"/></svg></span>
          <h4 class="check__title">Amazing Service</h4>
          <p class="check__text">We are committed to delivering Amazing Service to your small business, at every point of contact you make with Halvern. This is our brand promise.</p></li>
      </ul>
    </article>

    <article class="panel services">
      <div class="brand services__brand brand--on-dark"><span class="brand__dot"></span>Pelmora Systems</div>
      <h3 class="services__heading">Our Services</h3>
      <ul class="services__list">
        <li class="service"><span class="service__icon"><svg width="18" height="18" viewBox="0 0 12 12"><path d="M3 1l2 2.5-1.2 1.2a7 7 0 003.5 3.5L8.5 7 11 9l-1.5 2C5 11 1 7 1 2.5z" fill="#fff"/></svg></span>
          <div><h4 class="service__title">Business VoIP</h4><p class="service__text">Use the same business number on your desk phone, mobile app and computer.</p></div></li>
        <li class="service"><span class="service__icon"><svg width="18" height="18" viewBox="0 0 12 12"><path d="M1 2h10v6H5l-3 2.5V8H1z" fill="#fff"/></svg></span>
          <div><h4 class="service__title">Text Messaging</h4><p class="service__text">Send and receive texts from your business line with any team member.</p></div></li>
        <li class="service"><span class="service__icon"><svg width="18" height="18" viewBox="0 0 12 12"><rect x="1" y="3" width="7" height="6" rx="1" fill="#fff"/><path d="M8 5l3-2v6L8 7z" fill="#fff"/></svg></span>
          <div><h4 class="service__title">Video Conferencing</h4><p class="service__text">Meet face to face with clients and colleagues in high definition video.</p></div></li>
        <li class="service"><span class="service__icon"><svg width="18" height="18" viewBox="0 0 12 12"><rect x="1" y="2.5" width="10" height="7" fill="none" stroke="#fff" stroke-width="1.4"/><path d="M1 3l5 3.5L11 3" fill="none" stroke="#fff" stroke-width="1.2"/></svg></span>
          <div><h4 class="service__title">Voicemail to Email</h4><p class="service__text">Get every voicemail delivered straight to your inbox as an audio file.</p></div></li>
        <li class="service"><span class="service__icon"><svg width="18" height="18" viewBox="0 0 12 12"><rect x="2" y="1" width="8" height="10" rx="1" fill="none" stroke="#fff" stroke-width="1.4"/><path d="M4 4h4M4 6h4M4 8h2" stroke="#fff"/></svg></span>
          <div><h4 class="service__title">Call Queues</h4><p class="service__text">Route callers to the right department and keep them on hold with music.</p></div></li>
        <li class="service"><span class="service__icon"><svg width="18" height="18" viewBox="0 0 12 12"><path d="M2 6c0-2 1.2-3 2.2-3S6 6 6 6s.8 3 1.8 3S10 8 10 6 8.8 3 7.8 3 6 6 6 6 5.2 9 4.2 9 2 8 2 6z" fill="none" stroke="#fff" stroke-width="1.3"/></svg></span>
          <div><h4 class="service__title">Unlimited Calling</h4><p class="service__text">Unlimited calls across the US and Canada with free conference lines.</p></div></li>
      </ul>
    </article>

    <article class="panel extras">
      <ul class="checklist">
        <li class="check"><span class="check__tick"><svg width="8" height="8" viewBox="0 0 8 8"><path d="M1 4l2 2 4-4" fill="none" stroke="#fff" stroke-width="1.5"/></svg></span>
          <h4 class="check__title">Mobile friendly</h4>
          <p class="check__text">Run your small business from anywhere with the mobile app. Make calls, send texts and check voicemail right from your smartphone.</p></li>
        <li class="check"><span class="check__tick"><svg width="8" height="8" viewBox="0 0 8 8"><path d="M1 4l2 2 4-4" fill="none" stroke="#fff" stroke-width="1.5"/></svg></span>
          <h4 class="check__title">HD quality</h4>
          <p class="check__text">Experience crystal clear HD voice quality with every call. Your customers will hear the difference and never worry about dropped calls.</p></li>
        <li class="check"><span class="check__tick"><svg width="8" height="8" viewBox="0 0 8 8"><path d="M1 4l2 2 4-4" fill="none" stroke="#fff" stroke-width="1.5"/></svg></span>
          <h4 class="check__title">Powerful features</h4>
          <p class="check__text">Small business VoIP features without the hefty price tag. Auto attendant, call forwarding, hold music and much more.</p></li>
        <li class="check"><span class="check__tick"><svg width="8" height="8" viewBox="0 0 8 8"><path d="M1 4l2 2 4-4" fill="none" stroke="#fff" stroke-width="1.5"/></svg></span>
          <h4 class="check__title">Easy to use</h4>
          <p class="check__text">Our phones are as easy to use as the ones you have now. No IT department is needed to get started in minutes.</p></li>
        <li class="check"><span class="check__tick"><svg width="8" height="8" viewBox="0 0 8 8"><path d="M1 4l2 2 4-4" fill="none" stroke="#fff" stroke-width="1.5"/></svg></span>
          <h4 class="check__title">Honest pricing</h4>
          <p class="check__text">Customers know what they are paying for. No contracts, no hidden fees. You can cancel your service at any time, hassle-free.</p></li>
      </ul>
      <svg class="shape" style="top:500px;height:242px" viewBox="0 0 320 242" aria-hidden="true">
        <polygon points="0,30 198,0 320,16 320,242 0,242" fill="#3b3b3d"/>
      </svg>
      <div class="photo extras__photo" role="img" aria-label="Business team meeting around a conference table"></div>
    </article>
  </section>

</main>
</body>
</html>
```